Artisan Bread Company Needs a Poster

We need a poster design (with the measurements 1 Ft Horizontal, by 2 Ft Vertical) This poster is to advertise "Hollin's Loaf" and draw attention to the new product. The poster MUST have the "Hollin's Loaf Logo" provided below. (Signage.ai) The lettering below that says "local, organic, sourdough" can be moved around. It must be somewhere on the poster though. The poster is to inform people that the bread is Organic, local, and sourdough.
Feel free to use any pictures that would work.
The poster should have the text-- "Hollin's Loaf is made from 100% Organic flour, grown and milled in Ontario. Hollin's Loaf uses a traditional sourdough method with a long fermentation time, to help with digestibility. All of our breads are hand shaped, and hearth baked in a scorching hot oven."
Target Market(s)
People conscious about their eating habits, anywhere from 24-60. Think yoga moms.
Industry/Entity Type
Bakery
Requirements
Must have
- The poster MUST have the "Hollin's Loaf Logo" provided below. (Signage.ai) The lettering below that says "local, organic, sourdough" can be moved around. It must be somewhere on the poster though. The poster is to inform people that the bread is Organic, local, and sourdough.

```html
<!DOCTYPE html>
<html lang="en">
<head>
<meta charset="utf-8">
<title>Hollin's Loaf Poster</title>
<link href="https://fonts.googleapis.com/css2?family=Great+Vibes&family=PT+Serif:wght@400&display=swap" rel="stylesheet">
<style>
  :root {
    --board: #1f1f1f;
    --board-light: #2c2c2c;
    --chalk: #f4f1ea;
    --local: #ec7a6c;
    --organic: #8dc63f;
    --sourdough: #f2b43c;
    --crust-dark: #4a2c16;
    --crust: #a8672c;
    --crust-light: #d9a45c;
    --lettuce: #8fbf4a;
  }
  * { margin: 0; padding: 0; box-sizing: border-box; }
  html, body { width: 1200px; height: 2400px; overflow: hidden; background: var(--board); }
  .poster {
    position: relative;
    width: 1200px;
    height: 2400px;
    overflow: hidden;
    background: radial-gradient(ellipse at 50% 40%, var(--board-light) 0%, var(--board) 70%);
    font-family: "PT Serif", Georgia, serif;
    color: var(--chalk);
  }
  .frame {
    position: absolute;
    left: 19px; top: 19px; right: 19px; bottom: 19px;
    border: 3px solid var(--chalk);
  }
  .brand {
    position: absolute;
    top: 220px; left: 0; width: 100%;
    text-align: center;
    font-size: 120px;
    line-height: 1;
    color: var(--chalk);
  }
  .intro {
    position: absolute;
    top: 512px; left: 192px; width: 816px;
    text-align: center;
    font-size: 26px;
    line-height: 1.3;
    color: var(--chalk);
  }
  .claim {
    position: absolute;
    left: 0; width: 100%;
    text-align: center;
    font-family: "Great Vibes", cursive;
    font-size: 104px;
    line-height: 1;
  }
  .claim--local { top: 820px; color: var(--local); }
  .claim--organic { top: 1066px; color: var(--organic); }
  .claim--sourdough { top: 1334px; color: var(--sourdough); }
  .bread-photo {
    position: absolute;
    left: 0; top: 1600px; width: 1200px; height: 800px;
    background:
      radial-gradient(ellipse at 88% 10%, var(--lettuce) 0%, rgba(143,191,74,0) 22%),
      radial-gradient(ellipse at 30% 40%, var(--crust-light) 0%, rgba(217,164,92,0) 45%),
      radial-gradient(ellipse at 70% 60%, var(--crust) 0%, rgba(168,103,44,0) 50%),
      linear-gradient(180deg, rgba(74,44,22,0) 0%, var(--crust-dark) 12%, var(--crust) 55%, var(--crust-dark) 100%);
  }
</style>
</head>
<body>
  <main class="poster">
    <div class="frame"></div>
    <h1 class="brand">Hollin's Loaf</h1>
    <p class="intro">Hollin's Loaf is made from 100% Organic flour, grown and milled in Ontario. Hollin's Loaf uses a traditional sourdough method with a long fermentation time, to help with digestibility. All of our breads are hand shaped, and hearth baked in a scorching hot oven</p>
    <p class="claim claim--local">-Local-</p>
    <p class="claim claim--organic">-Organic-</p>
    <p class="claim claim--sourdough">-Sourdough-</p>
    <div class="bread-photo" role="img" aria-label="Pile of rustic hearth-baked sourdough loaves with flour-dusted crusts and fresh green lettuce leaves"></div>
  </main>
</body>
</html>
```